Promotion flyer for chair massage

What i need is a design for a 2 page flyer. Im gonna give it to a company so their employe can learn about the service and how they can take an appointements with us. The text is in french because i work in a french company.
On first page(FRONT PAGE) i want the name of the company VELORAMAX inc.
and bellow : Massothérapie sur chaise en entreprise
On the second page(INSIDE) i want the benefits :
Les Bienfaits
- DIMINUTION DU STRESS
- AMÉLIORATION DU BIEN-ÊTRE PHYSIQUE ET PSYCHOLOGIQUE
- AUGMENTATION DE L’ÉNERGIE
- SOULAGE LES MAUX DE DOS ET DE TÊTE
- AMÉLIORE VOTRE QUALITÉ DE SOMMEIL
On the third page (INSIDE) I want the steps to take an appointment :
Obtenez votre massage en quelques clics
1. Allez sur https://www.bookalyte.example/veloramax
2. Choisir le nombre de minute désirer (10-15-20-30)
3. Choisir votre thérapeute
4. Choisir votre emplacement (lieu de travail)
5. Choisir votre plage horaire
6. Remplir votre fiche (Prénom-Nom-Email-#téléphone)
7. Aussi simple que ça !! À bientôt !
On the final page i want the text so they can contact me :
CONTACTEZ-NOUS
Mail : Info@veloramax.example
Tél. 514-276-9032
Site web : Veloramax.example
If you can respect the same kind of design that i already did in the past i would love it :)
Bank employee
Massage Therapy

```html
<!DOCTYPE html>
<html lang="fr">
<head>
<meta charset="utf-8">
<title>VELORAMAX inc. – Massothérapie sur chaise en entreprise</title>
<link rel="stylesheet" href="https://fonts.googleapis.com/css2?family=Roboto+Condensed:wght@400;700&family=Roboto:wght@400;500;700&display=swap">
<style>
  :root{
    --ink:#2b2b2e;
    --ink-deep:#1f1f22;
    --blue:#1d60ab;
    --paper:#ffffff;
    --mist-dark:#c9c9cc;
    --canvas:#eeeeee;
  }
  *{box-sizing:border-box;margin:0;padding:0}
  html,body{width:1200px;height:800px;overflow:hidden;background:var(--canvas)}
  body{font-family:"Roboto",Arial,sans-serif;position:relative}
  .spread{position:absolute;top:202px;width:560px;height:396px;box-shadow:0 10px 30px rgba(0,0,0,.22)}
  .spread--cover{left:20px}
  .spread--inside{left:620px}
  .spread-art{position:absolute;inset:0;width:560px;height:396px;display:block}
  .spread::after{content:"";position:absolute;left:279px;top:0;width:2px;height:100%;background:linear-gradient(90deg,rgba(0,0,0,.18),rgba(255,255,255,.15))}
  .t{position:absolute}
  .brand-name{font-family:"Roboto Condensed",Arial,sans-serif;font-weight:700;letter-spacing:.5px}
  .brand-name--dark{color:var(--ink)}
  .brand-name--light{color:var(--paper)}
  .contact{left:24px;top:268px;color:var(--paper)}
  .contact-title{font-family:"Roboto Condensed",Arial,sans-serif;font-weight:700;font-size:18px;letter-spacing:.3px}
  .contact-line{font-size:10px;margin-top:4px}
  .contact-phone{font-family:"Roboto Condensed",Arial,sans-serif;font-weight:700;font-size:17px;margin-top:2px}
  .url{font-size:9px;color:var(--paper);letter-spacing:.3px}
  .headline{right:16px;top:78px;text-align:right;color:var(--paper);font-family:"Roboto Condensed",Arial,sans-serif;font-weight:700;line-height:1}
  .headline-top{font-size:17px;font-weight:400}
  .headline-main{font-size:28px}
  .headline-sub{font-size:17px;font-weight:400}
  .title-benefits{left:18px;top:30px;font-family:"Roboto Condensed",Arial,sans-serif;font-weight:700;font-size:36px;color:var(--paper);letter-spacing:.5px}
  .benefit{position:absolute;width:120px;text-align:center;font-family:"Roboto Condensed",Arial,sans-serif;font-weight:700;font-size:8.5px;line-height:1.15;color:var(--ink);text-transform:uppercase}
  .benefit--wide{width:160px}
  .steps-title{left:300px;top:14px;font-family:"Roboto Condensed",Arial,sans-serif;font-weight:700;font-size:15px;color:var(--paper)}
  .steps{position:absolute;left:300px;top:112px;list-style:none;counter-reset:step}
  .step{counter-increment:step;display:flex;align-items:center;gap:6px;font-size:8.2px;color:var(--ink);margin-bottom:5.5px;white-space:nowrap}
  .step::before{content:counter(step);width:11px;height:11px;border-radius:50%;background:var(--blue);color:var(--paper);font-size:7px;font-weight:700;display:flex;align-items:center;justify-content:center;flex:none}
</style>
</head>
<body>

<section class="spread spread--cover">
  <svg class="spread-art" viewBox="0 0 560 396">
    <defs>
      <linearGradient id="g-mist" x1="0" y1="0" x2="1" y2="1">
        <stop offset="0" stop-color="#f2f2f3"/><stop offset="1" stop-color="#cfcfd2"/>
      </linearGradient>
      <linearGradient id="g-studio" x1="0" y1="0" x2="1" y2="1">
        <stop offset="0" stop-color="#cfc9c2"/><stop offset=".55" stop-color="#8d8780"/><stop offset="1" stop-color="#4a4744"/>
      </linearGradient>
      <linearGradient id="g-therapist" x1="0" y1="0" x2="1" y2="0">
        <stop offset="0" stop-color="#7c8a91"/><stop offset=".5" stop-color="#a9b4b8"/><stop offset="1" stop-color="#d8dcdd"/>
      </linearGradient>
      <linearGradient id="g-circle" x1="0" y1="0" x2="1" y2="1">
        <stop offset="0" stop-color="#d9d4cf"/><stop offset="1" stop-color="#6f6b68"/>
      </linearGradient>
    </defs>

    <rect x="0" y="0" width="280" height="396" fill="var(--ink)"/>
    <rect x="0" y="0" width="280" height="230" fill="url(#g-studio)" role="img" aria-label="Photo : massothérapeute donnant un massage sur chaise dans un atelier lumineux"/>
    <path d="M0,196 Q140,150 280,118 L280,134 Q140,168 0,214 Z" fill="var(--blue)"/>
    <path d="M0,214 Q140,168 280,134 L280,142 Q140,176 0,222 Z" fill="var(--paper)"/>
    <path d="M0,222 Q140,176 280,142 L280,396 L0,396 Z" fill="var(--ink)"/>
    <path d="M0,330 Q150,390 280,300 L280,312 Q150,398 0,344 Z" fill="var(--blue)"/>
    <path d="M0,344 Q150,398 280,312 L280,396 L0,396 Z" fill="var(--ink-deep)"/>

    <rect x="280" y="0" width="280" height="396" fill="url(#g-mist)"/>
    <rect x="280" y="0" width="280" height="62" fill="var(--paper)"/>
    <path d="M280,62 L560,62 L560,200 Q430,190 280,252 Z" fill="url(#g-therapist)" role="img" aria-label="Photo : massothérapeute souriant, bras croisés"/>
    <path d="M280,72 Q420,44 560,40 L560,60 Q420,66 280,112 Z" fill="var(--ink)"/>
    <path d="M280,112 Q420,66 560,60 L560,68 Q420,76 280,120 Z" fill="var(--blue)"/>
    <path d="M280,62 Q420,40 560,34 L560,40 Q420,44 280,72 Z" fill="var(--mist-dark)"/>
    <path d="M280,252 Q430,190 560,200 L560,210 Q430,200 280,262 Z" fill="var(--blue)"/>
    <circle cx="350" cy="286" r="44" fill="url(#g-circle)" stroke="var(--ink)" stroke-width="3" role="img" aria-label="Photo : massage de la nuque"/>
    <circle cx="470" cy="272" r="64" fill="url(#g-circle)" stroke="var(--ink)" stroke-width="3" role="img" aria-label="Photo : massage des épaules d'un employé"/>
    <path d="M280,352 Q430,340 560,290 L560,304 Q430,352 280,364 Z" fill="var(--blue)"/>
    <path d="M280,364 Q430,352 560,304 L560,396 L280,396 Z" fill="var(--ink)"/>
  </svg>

  <div class="t brand-name brand-name--light" style="left:24px;top:234px;font-size:19px">VELORAMAX inc.</div>

  <div class="t contact">
    <div class="contact-title">CONTACTEZ-NOUS</div>
    <div class="contact-line">Mail : Info@veloramax.example</div>
    <div class="contact-phone">Tél. 514-276-9032</div>
  </div>
  <div class="t url" style="left:150px;top:376px">www.veloramax.example</div>

  <div class="t brand-name brand-name--dark" style="right:18px;top:18px;font-size:17px">VELORAMAX inc.</div>

  <h1 class="t headline">
    <span class="headline-top">Massothérapie</span><br>
    <span class="headline-main">sur chaise</span><br>
    <span class="headline-sub">en entreprise</span>
  </h1>
  <div class="t url" style="left:300px;top:376px">www.veloramax.example</div>
</section>

<section class="spread spread--inside">
  <svg class="spread-art" viewBox="0 0 560 396">
    <defs>
      <linearGradient id="g-inner" x1="0" y1="0" x2="1" y2="1">
        <stop offset="0" stop-color="#f3f3f4"/><stop offset="1" stop-color="#cdcdd0"/>
      </linearGradient>
      <linearGradient id="g-back" x1="0" y1="0" x2="1" y2="1">
        <stop offset="0" stop-color="#b98a74"/><stop offset=".6" stop-color="#8a4f4a"/><stop offset="1" stop-color="#5a3433"/>
      </linearGradient>
    </defs>
    <rect x="0" y="0" width="560" height="396" fill="url(#g-inner)"/>

    <path d="M0,0 L280,0 L280,62 Q140,74 0,108 Z" fill="var(--ink)"/>
    <path d="M0,108 Q140,74 280,62 L280,70 Q140,82 0,116 Z" fill="var(--blue)"/>
    <path d="M0,360 Q140,392 280,370 L280,396 L0,396 Z" fill="var(--ink)"/>
    <path d="M0,352 Q140,384 280,362 L280,370 Q140,392 0,360 Z" fill="var(--blue)"/>

    <g class="benefit-icon" transform="translate(0,-10)">
      <circle cx="72" cy="170" r="28" fill="var(--blue)"/>
      <path d="M72,184 L72,166 M72,172 Q58,170 60,156 Q72,158 72,172 M72,170 Q86,166 84,154 Q72,158 72,170" fill="none" stroke="var(--paper)" stroke-width="2" stroke-linecap="round" stroke-linejoin="round"/>
    </g>
    <g class="benefit-icon" transform="translate(0,-10)">
      <circle cx="200" cy="132" r="28" fill="var(--blue)"/>
      <g fill="none" stroke="var(--paper)" stroke-width="2" stroke-linecap="round" stroke-linejoin="round">
        <path d="M190,146 L190,136 Q186,132 188,126 Q192,114 204,116 Q214,120 212,130 L214,134 L210,136 L210,142 L204,142 L204,146"/>
        <circle cx="200" cy="127" r="5"/>
      </g>
    </g>
    <g class="benefit-icon" transform="translate(0,-14)">
      <circle cx="208" cy="232" r="28" fill="var(--blue)"/>
      <g fill="none" stroke="var(--paper)" stroke-width="2" stroke-linecap="round" stroke-linejoin="round">
        <circle cx="200" cy="220" r="4"/>
        <path d="M200,226 L200,238 L212,238 L212,246 M194,232 L206,232 M216,222 L216,246 M196,246 L220,246"/>
      </g>
    </g>
    <g class="benefit-icon" transform="translate(0,-20)">
      <circle cx="76" cy="282" r="28" fill="var(--blue)"/>
      <path d="M70,292 L70,288 Q62,282 64,274 Q68,266 76,266 Q84,266 88,274 Q90,282 82,288 L82,292 Z M71,296 L81,296 M60,266 L56,262 M92,266 L96,262 M76,260 L76,255" fill="none" stroke="var(--paper)" stroke-width="2" stroke-linecap="round" stroke-linejoin="round"/>
    </g>
    <g class="benefit-icon" transform="translate(0,-24)">
      <circle cx="208" cy="322" r="26" fill="var(--blue)"/>
      <g fill="none" stroke="var(--paper)" stroke-width="2" stroke-linecap="round" stroke-linejoin="round">
        <path d="M192,332 L192,312 M192,326 L224,326 L224,332 M198,320 L222,320 L222,326"/>
        <circle cx="200" cy="316" r="3"/>
      </g>
    </g>

    <path d="M280,0 L560,0 L560,38 Q420,58 280,100 Z" fill="var(--ink)"/>
    <path d="M280,100 Q420,58 560,38 L560,46 Q420,66 280,108 Z" fill="var(--blue)"/>
    <path d="M280,396 L280,330 Q420,250 560,236 L560,396 Z" fill="url(#g-back)" role="img" aria-label="Photo : mains d'un massothérapeute massant le dos d'une personne"/>
    <path d="M280,322 Q420,242 560,228 L560,236 Q420,250 280,330 Z" fill="var(--blue)"/>
    <path d="M280,376 Q420,392 560,356 L560,396 L280,396 Z" fill="var(--ink)"/>
    <path d="M280,370 Q420,386 560,350 L560,356 Q420,392 280,376 Z" fill="var(--blue)"/>
  </svg>

  <h2 class="t title-benefits">LES BIENFAITS</h2>
  <p class="benefit" style="left:12px;top:194px">Diminution du stress</p>
  <p class="benefit" style="left:140px;top:154px">Amélioration du bien-être physique et psychologique</p>
  <p class="benefit" style="left:148px;top:252px">Soulage les maux de dos et de tête</p>
  <p class="benefit" style="left:16px;top:296px">Augmentation de l’énergie</p>
  <p class="benefit benefit--wide" style="left:128px;top:330px">Améliore votre qualité de sommeil</p>

  <h2 class="t steps-title">Obtenez votre massage en quelques clics</h2>
  <ol class="steps">
    <li class="step">Allez sur https://www.bookalyte.example/veloramax</li>
    <li class="step">Choisir le nombre de minute désirer (10-15-20-30)</li>
    <li class="step">Choisir votre thérapeute</li>
    <li class="step">Choisir votre emplacement (lieu de travail)</li>
    <li class="step">Choisir votre plage horaire</li>
    <li class="step">Remplir votre fiche (Prénom-Nom-Email-#téléphone)</li>
    <li class="step">Aussi simple que ça !! À bientôt !</li>
  </ol>
</section>

</body>
</html>
```